Lawn Sign Design – Vextra

We need a clean, eye-catching 18" x 24" lawn sign for Vextra that effectively communicates our core message while maintaining strong brand consistency.

Key Elements to Include:
Tagline (Main Focus): Upgrade Your Roof Without Replacing It
Website: www.tryvextra-example.com
Phone Number: (877) VEXTRA-GO
PRQT License Number: 4830517
Vextra Logo & Branding: Ensure the logo, corporate colors, and custom font are used consistently to align with our existing branding.

Design Guidelines:
Simple & High-Impact: The tagline should be the most prominent element on the sign, drawing immediate attention.
Easy Readability: Use a bold, clean design with high contrast for quick readability from a distance.
Balanced Layout: Place supporting details (website, phone number, and PRQT number) in a visually clear but secondary position to the tagline.
Professional & Modern: The sign should reflect credibility and innovation in the roofing industry.

Deliverables:
High-resolution print-ready files (CMYK)
A digital proof for review before finalizing
The final design should make a strong impression with minimal text, ensuring that anyone passing by can instantly grasp what we offer.

I am including our custom font. To get an hexagon in our name, simply type the $ after the 'O" Please use this font for anything you type.

```html
<!DOCTYPE html>
<html lang="en">
<head>
<meta charset="utf-8">
<title>Vextra Lawn Sign</title>
<link rel="stylesheet" href="https://fonts.googleapis.com/css2?family=Nunito:wght@800;900&display=swap">
<style>
  :root {
    --brand-blue: #12509a;
    --sign-white: #f5f5f4;
    --backdrop: #dde2e8;
    --text-light: #ffffff;
  }
  * { margin: 0; padding: 0; box-sizing: border-box; }
  html, body {
    width: 1200px;
    height: 862px;
    overflow: hidden;
    background: var(--backdrop);
    font-family: "Nunito", sans-serif;
  }
  .lawn-sign {
    position: absolute;
    left: 30px;
    top: 77px;
    width: 1140px;
    height: 708px;
    background: var(--sign-white);
    color: var(--brand-blue);
    box-shadow: 0 6px 18px rgba(20, 40, 70, 0.18);
  }
  .brand {
    position: absolute;
    top: 95px;
    left: 0;
    width: 100%;
    height: 190px;
    display: flex;
    align-items: center;
    justify-content: center;
    gap: 44px;
  }
  .brand-mark {
    width: 150px;
    height: 150px;
    background: var(--brand-blue);
  }
  .brand-name {
    font-size: 120px;
    font-weight: 900;
    letter-spacing: 4px;
    line-height: 1;
    color: var(--brand-blue);
  }
  .detail {
    position: absolute;
    left: 0;
    width: 100%;
    text-align: center;
    font-weight: 800;
    line-height: 1;
    white-space: nowrap;
  }
  .website { top: 350px; font-size: 40px; letter-spacing: 1px; }
  .phone { top: 405px; font-size: 80px; letter-spacing: 2px; font-weight: 900; }
  .license { top: 492px; font-size: 46px; letter-spacing: 1px; }
  .tagline-band {
    position: absolute;
    left: 0;
    bottom: 0;
    width: 100%;
    height: 95px;
    background: var(--brand-blue);
    display: flex;
    align-items: center;
    justify-content: center;
  }
  .tagline {
    color: var(--text-light);
    font-size: 44px;
    font-weight: 800;
    letter-spacing: 1.5px;
    white-space: nowrap;
  }
</style>
</head>
<body>
  <main class="lawn-sign">
    <div class="brand">
      <span class="brand-mark" aria-hidden="true"></span>
      <span class="brand-name">VEXTRA</span>
    </div>
    <p class="detail website">www.tryvextra-example.com</p>
    <p class="detail phone">Tel : (877) VEXTRA-GO</p>
    <p class="detail license">PRQT License Number: 4830517</p>
    <div class="tagline-band">
      <p class="tagline">Upgrade Your Roof Without Replacing It</p>
    </div>
  </main>
</body>
</html>
```